Cover Design For eBook "Norla"

I need two e-book covers with the same look and feel:

first one:
title
THE NORLA CAMPAIGN
subtitle
IGNITE DIGITAL GIVING
author
MERIDAN DONATIONS (just include the logo I attach)

second eBook
title
THE NORLA SYSTEM
subtitle
5 STEPS TO IGNITE YOUR CHURCH'S DIGITAL GIVING
author
MERIDAN DONATIONS (just include the log I attach)

Industry/Entity Type

Digital

Colors
f04a50
f68e4e
faa54b
ffcf3e

Requirements
Must have
• the MERIDAN DONATIONS LOGO I attached at the bottom of the design.
• There needs to be some type of spark coming off of one of the letters in NORLA
Nice to have
• I'd love to have a horizontal and vertical layout

```html
<!DOCTYPE html>
<html lang="en">
<head>
<meta charset="utf-8">
<title>The Norla Campaign &amp; The Norla System — eBook Covers</title>
<link rel="stylesheet" href="https://fonts.googleapis.com/css2?family=Archivo+Black&family=Montserrat:wght@700;800&display=swap">
<style>
  :root {
    --page: #ffffff;
    --ink: #0a0a0a;
    --band: #070707;
    --gold-light: #ffe27a;
    --gold: #ffcf3e;
    --amber: #faa54b;
    --orange: #f68e4e;
    --red: #f04a50;
    --ember-dark: #140403;
    --ember-mid: #4a0f07;
    --spark-white: #fffbe6;
    --logo-text: #222222;
  }
  * { margin: 0; padding: 0; box-sizing: border-box; }
  html, body {
    width: 1200px; height: 474px; overflow: hidden;
    background: var(--page);
  }
  .covers { position: relative; width: 1200px; height: 474px; }
  .cover {
    position: absolute; top: 0; height: 474px; overflow: hidden;
    background: var(--ink);
  }
  .cover--campaign { left: 0; width: 593px; }
  .cover--system { left: 608px; width: 592px; }

  .cover__sparkler-sky {
    position: absolute; left: 0; top: 0; width: 100%; height: 240px;
    background:
      radial-gradient(ellipse 55% 60% at 62% 70%, rgba(240,74,80,0.5), transparent 70%),
      radial-gradient(ellipse 35% 45% at 78% 60%, rgba(250,165,75,0.3), transparent 70%),
      linear-gradient(180deg, var(--ember-dark) 0%, var(--ember-mid) 70%, #7a160a 100%);
  }
  .cover__band {
    position: absolute; left: 0; top: 240px; width: 100%; height: 132px;
    background: var(--band);
  }
  .cover__sparkler-glow {
    position: absolute; left: 0; top: 372px; width: 100%; height: 102px;
    background:
      radial-gradient(ellipse 60% 90% at 50% 15%, rgba(255,255,230,0.85), transparent 70%),
      linear-gradient(180deg, var(--red) 0%, var(--orange) 30%, var(--amber) 60%, var(--gold) 100%);
  }

  .title {
    position: absolute; left: 0; top: 0; width: 100%; height: 280px;
    font-size: inherit;
  }
  .title__art { display: block; width: 100%; height: 280px; overflow: visible; }
  .title__word {
    font-family: "Archivo Black", "Arial Black", sans-serif;
    text-transform: uppercase;
  }
  .spark line { stroke: var(--spark-white); stroke-linecap: round; }

  .subtitle {
    position: absolute; left: 0; width: 100%;
    font-family: "Montserrat", Arial, sans-serif; font-weight: 800;
    color: var(--gold); text-align: center; text-transform: uppercase;
    letter-spacing: 1.2px;
  }
  .cover--campaign .subtitle { top: 287px; font-size: 26px; line-height: 36px; }
  .cover--system .subtitle { top: 268px; font-size: 25px; line-height: 38px; }

  .author {
    position: absolute; left: 0; top: 412px; width: 100%;
    display: flex; align-items: center; justify-content: center; gap: 9px;
  }
  .author__dot { width: 30px; height: 30px; border-radius: 50%; background: var(--red); }
  .author__name {
    font-family: "Montserrat", Arial, sans-serif; font-weight: 700;
    font-size: 20px; color: var(--logo-text); letter-spacing: 0.3px;
  }
</style>
</head>
<body>
<svg width="0" height="0" style="position:absolute" aria-hidden="true">
  <defs>
    <linearGradient id="title-gold" x1="0" y1="0" x2="0" y2="1">
      <stop offset="0" stop-color="#ffe27a"/>
      <stop offset="0.45" stop-color="#ffcf3e"/>
      <stop offset="0.8" stop-color="#faa54b"/>
      <stop offset="1" stop-color="#f68e4e"/>
    </linearGradient>
    <filter id="title-depth" x="-10%" y="-20%" width="120%" height="150%">
      <feDropShadow dx="2" dy="2" stdDeviation="0" flood-color="#a3561a"/>
      <feDropShadow dx="2" dy="2" stdDeviation="0" flood-color="#6b3210"/>
      <feDropShadow dx="0" dy="0" stdDeviation="5" flood-color="#ffcf3e" flood-opacity="0.35"/>
    </filter>
    <radialGradient id="spark-glow">
      <stop offset="0" stop-color="#ffffff"/>
      <stop offset="0.35" stop-color="#ffe27a" stop-opacity="0.9"/>
      <stop offset="1" stop-color="#ffcf3e" stop-opacity="0"/>
    </radialGradient>
    <g id="spark-burst">
      <circle r="16" fill="url(#spark-glow)"/>
      <line x1="0" y1="-4" x2="0" y2="-30" stroke-width="2"/>
      <line x1="4" y1="-2" x2="26" y2="-18" stroke-width="2"/>
      <line x1="5" y1="1" x2="32" y2="4" stroke-width="1.6"/>
      <line x1="3" y1="4" x2="20" y2="22" stroke-width="1.4"/>
      <line x1="-4" y1="-2" x2="-22" y2="-20" stroke-width="1.6"/>
      <line x1="-5" y1="1" x2="-26" y2="6" stroke-width="1.4"/>
      <line x1="12" y1="-28" x2="16" y2="-38" stroke-width="1.2"/>
      <line x1="34" y1="-12" x2="42" y2="-16" stroke-width="1.2"/>
    </g>
  </defs>
</svg>

<main class="covers">
  <section class="cover cover--campaign">
    <div class="cover__sparkler-sky" role="img" aria-label="Dark red background with a burning sparkler throwing sparks"></div>
    <div class="cover__band"></div>
    <div class="cover__sparkler-glow" role="img" aria-label="Bright orange and yellow sparkler burst"></div>
    <h1 class="title">
      <svg class="title__art" viewBox="0 0 593 280" aria-label="The Norla Campaign">
        <g fill="url(#title-gold)" filter="url(#title-depth)">
          <text class="title__word" x="200" y="105" font-size="78" textLength="135" lengthAdjust="spacingAndGlyphs" transform="rotate(-3 200 105)">The</text>
          <text class="title__word" x="160" y="166" font-size="80" textLength="270" lengthAdjust="spacingAndGlyphs" transform="rotate(-4 160 166)">Norla</text>
          <text class="title__word" x="80" y="262" font-size="86" textLength="440" lengthAdjust="spacingAndGlyphs" transform="rotate(-7 80 262)">Campaign</text>
        </g>
        <use class="spark" href="#spark-burst" x="414" y="104" stroke="#fffbe6"/>
      </svg>
    </h1>
    <p class="subtitle">Ignite Digital Giving</p>
    <div class="author"><span class="author__dot"></span><span class="author__name">MERIDAN DONATIONS</span></div>
  </section>

  <section class="cover cover--system">
    <div class="cover__sparkler-sky" role="img" aria-label="Dark red background with a burning sparkler throwing sparks"></div>
    <div class="cover__band"></div>
    <div class="cover__sparkler-glow" role="img" aria-label="Bright orange and yellow sparkler burst"></div>
    <h1 class="title">
      <svg class="title__art" viewBox="0 0 592 280" aria-label="The Norla System">
        <g fill="url(#title-gold)" filter="url(#title-depth)">
          <text class="title__word" x="200" y="105" font-size="78" textLength="140" lengthAdjust="spacingAndGlyphs" transform="rotate(-3 200 105)">The</text>
          <text class="title__word" x="145" y="165" font-size="80" textLength="250" lengthAdjust="spacingAndGlyphs" transform="rotate(-4 145 165)">Norla</text>
          <text class="title__word" x="135" y="252" font-size="86" textLength="315" lengthAdjust="spacingAndGlyphs" transform="rotate(-9 135 252)">System</text>
        </g>
        <use class="spark" href="#spark-burst" x="380" y="104" stroke="#fffbe6"/>
      </svg>
    </h1>
    <p class="subtitle">5 Steps to Ignite Your<br>Church's Digital Giving</p>
    <div class="author"><span class="author__dot"></span><span class="author__name">MERIDAN DONATIONS</span></div>
  </section>
</main>
</body>
</html>
```